Paper Lanterns Fading ---Marla Quindstrom; EP cover

I am a pop artist and need my name and title of the EP designed onto professional pictures.(Paper Lanterns Fading---Marla Quindstrom) I am open to color for lettering and other design elements. I'd really like something that compliments the photo(s)! To get a feel for what I'm looking for-- reference past CD covers from pop artists like- Tessaly Vornet, Dana Prewitt, Lira Moskin, etc. Can't wait to see what you design!

Font styles to use
Serif
Sans Serif
Decorative
Script

Requirements
Must have
• I would like very little alteration to the pictures other than fitting pictures to the dimensions required for the CD cover. Some softening or a little bit of blurring to the picture is ok.
Nice to have
• My initial thought was to keep everything grayscale to match the photos, but if you feel so inspired--create!
Should not have
• No flashy lettering

```html
<!DOCTYPE html>
<html lang="en">
<head>
<meta charset="utf-8">
<title>Paper Lanterns Fading — Marla Quindstrom</title>
<link rel="stylesheet" href="https://fonts.googleapis.com/css2?family=Oswald:wght@500&family=Cormorant+SC:wght@500&display=swap">
<style>
  :root {
    --page-bg: #e6e6e6;
    --cover-dark: #1a1a1a;
    --cover-mid: #5a5a5a;
    --cover-light: #c4c4c4;
    --frame-line: #8c8c8c;
    --title-ink: #1c1c1c;
    --name-ink: #f2f2f2;
  }
  * { box-sizing: border-box; margin: 0; padding: 0; }
  html, body {
    width: 1200px;
    height: 960px;
    overflow: hidden;
    background: var(--page-bg);
  }
  .ep-cover {
    position: absolute;
    left: 160px;
    top: 40px;
    width: 880px;
    height: 880px;
    background: var(--cover-dark);
    overflow: hidden;
  }
  .cover-photo {
    position: absolute;
    inset: 0;
    background:
      radial-gradient(ellipse 32% 42% at 50% 48%, rgba(220,220,220,0.55), rgba(220,220,220,0) 70%),
      radial-gradient(ellipse 45% 30% at 52% 100%, rgba(10,10,10,0.9), rgba(10,10,10,0) 80%),
      linear-gradient(100deg, var(--cover-dark) 0%, var(--cover-mid) 45%, var(--cover-light) 100%);
  }
  .cover-frame {
    position: absolute;
    inset: 14px;
    border: 3px solid var(--frame-line);
    pointer-events: none;
  }
  .ep-title {
    position: absolute;
    top: 22px;
    left: 0;
    right: 0;
    text-align: center;
    font-family: "Oswald", sans-serif;
    font-weight: 500;
    font-size: 78px;
    line-height: 1.1;
    letter-spacing: 2px;
    text-transform: uppercase;
    color: var(--title-ink);
  }
  .artist-name {
    position: absolute;
    bottom: 26px;
    left: 0;
    right: 0;
    text-align: center;
    font-family: "Cormorant SC", serif;
    font-weight: 500;
    font-size: 46px;
    line-height: 1;
    letter-spacing: 1px;
    color: var(--name-ink);
  }
</style>
</head>
<body>
  <main class="ep-cover">
    <div class="cover-photo" role="img" aria-label="Black and white portrait photograph of the artist, head bowed, wavy shoulder-length hair, dark V-neck top with layered pendant necklaces, against a softly lit grey wall"></div>
    <div class="cover-frame"></div>
    <h1 class="ep-title">Paper Lanterns Fading</h1>
    <p class="artist-name">Marla Quindstrom</p>
  </main>
</body>
</html>
```